Tincture Design for Woman Owned CBD Branf

LumiVera is a luxery CBD brand for millennial women.

Our premium L Oil contains 500mg of full spectrum CBD derived from specially-sourced hemp for unparalleled purity and quality. Each dropper delivers approximately 20mg of CBD. Available in two flavors, Natural and Mint.

The goal is to design an aesthetically pleasing tincture (bottle dropper) with label and box. The final design should coincide with our brand guidelines and easily marketed for beauty consumers. We are looking for a clean design, the use of raised fonts and/or metallic is fine.

We have 4 other designs we'd like to work on with the winning designer.

Target Market(s)

Millennial Women, Income $75k+

Font styles to use
Other font styles liked:
• See Branding Sheet

Requirements
Must have
• Must follow brand guidelines (see attached for colors, font, etc)
Nice to have
• Raised font or Metallic Print

```html
<!DOCTYPE html>
<html lang="en">
<head>
<meta charset="utf-8">
<title>LumiVera L Oil – Tincture Labels and Boxes</title>
<link rel="stylesheet" href="https://fonts.googleapis.com/css2?family=Cormorant+Garamond:wght@400;500&family=Montserrat:wght@500;600;700&display=swap">
<style>
  :root {
    --forest: #1d5c51;
    --forest-leaf: #2a6a5e;
    --cream: #fbf4ea;
    --cream-leaf: #f3e6d2;
    --gold: #d9a449;
    --gold-light: #e8bd6c;
    --blush: #ecc9c0;
    --white: #ffffff;
    --mist: #f4f4f6;
    --ink-green: #1d5c51;
  }
  * { box-sizing: border-box; margin: 0; padding: 0; }
  html, body { width: 1035px; height: 1200px; overflow: hidden; }
  body { position: relative; background: var(--white); font-family: "Montserrat", sans-serif; }

  .row-labels { position: absolute; left: 0; top: 0; width: 1035px; height: 530px; background: var(--white); }
  .row-packs { position: absolute; left: 0; top: 530px; width: 1035px; height: 670px; background: var(--mist); }

  /* Shared label */
  .label {
    position: absolute; width: 13.3em; height: 18.5em; overflow: hidden;
    display: flex; flex-direction: column; align-items: center; text-align: center;
    padding-top: 1.3em;
  }
  .label--forest { background: var(--forest); }
  .label--cream { background: var(--cream); }

  .brand-name {
    font-family: "Cormorant Garamond", serif; font-weight: 400;
    font-size: 2.05em; letter-spacing: 0.02em; line-height: 1; text-transform: uppercase;
  }
  .label--forest .brand-name, .box--forest .brand-name { color: var(--white); }
  .label--cream .brand-name, .box--cream .brand-name { color: var(--ink-green); }

  .tagline {
    font-size: 0.36em; letter-spacing: 0.45em; font-weight: 600;
    color: var(--gold); margin-top: 0.9em; text-transform: uppercase;
  }
  .flavor {
    font-size: 0.85em; letter-spacing: 0.4em; font-weight: 600;
    margin-top: 1.3em; text-transform: uppercase; padding-left: 0.4em;
  }
  .label--forest .flavor, .box--forest .flavor { color: var(--white); }
  .label--cream .flavor, .box--cream .flavor { color: var(--ink-green); }

  .product-name {
    font-family: "Cormorant Garamond", serif; font-weight: 400;
    font-size: 4.6em; line-height: 1; margin-top: 0.05em; color: var(--gold);
    position: relative; z-index: 1;
  }
  .product-name--blush { color: var(--blush); }

  .leaf-motif {
    position: absolute; left: 10%; right: 10%; bottom: 1.6em; height: 5.5em;
    border-radius: 50% 50% 0 0 / 80% 80% 0 0;
  }
  .label--forest .leaf-motif, .box--forest .leaf-motif { background: linear-gradient(to top, var(--forest), var(--forest-leaf)); }
  .label--cream .leaf-motif, .box--cream .leaf-motif { background: linear-gradient(to top, var(--cream), var(--cream-leaf)); }

  .strength {
    position: absolute; left: 0; right: 0; bottom: 1.15em;
    font-size: 0.42em; letter-spacing: 0.15em; font-weight: 700; text-transform: uppercase;
  }
  .label--forest .strength { color: var(--white); }
  .label--cream .strength { color: var(--ink-green); }

  .label--small { font-size: 10px; top: 170px; }
  .label--large { font-size: 12.1px; top: 349px; }

  /* Boxes */
  .box {
    position: absolute; top: 57px; font-size: 17px; width: 13.5em; height: 32.4em;
    display: flex; flex-direction: column; align-items: center; text-align: center;
    padding-top: 2.7em; overflow: hidden;
  }
  .box--cream { background: var(--cream); }
  .box--forest { background: var(--forest); }
  .box .est {
    font-size: 0.4em; letter-spacing: 0.7em; font-weight: 600; text-transform: uppercase;
    color: var(--gold); padding-left: 0.7em;
  }
  .box .mark-dot {
    width: 1.4em; height: 1.4em; border-radius: 50%; border: 1px solid var(--gold);
    margin-top: 0.7em; margin-bottom: 0.8em;
  }
  .box .brand-name { font-size: 2.45em; }
  .box .tagline { font-size: 0.38em; margin-top: 1.4em; }
  .box .flavor { font-size: 0.95em; margin-top: 5.3em; }
  .box .product-name { font-size: 5.6em; margin-top: 0.1em; }
  .box .leaf-motif { height: 12em; bottom: 0; left: 14%; right: 14%; }
</style>
</head>
<body>
  <section class="row-labels" aria-label="Tincture labels">
    <article class="label label--forest label--small" style="left:60px">
      <h2 class="brand-name">LumiVera</h2>
      <p class="tagline">Premium CBD Products</p>
      <p class="flavor">Mint</p>
      <p class="product-name product-name--blush">L Oil</p>
      <div class="leaf-motif" role="img" aria-label="Faint hemp leaf motif"></div>
      <p class="strength">500mg Full Spectrum CBD</p>
    </article>
    <article class="label label--forest label--small" style="left:302px">
      <h2 class="brand-name">LumiVera</h2>
      <p class="tagline">Premium CBD Products</p>
      <p class="flavor">Mint</p>
      <p class="product-name">L Oil</p>
      <div class="leaf-motif" role="img" aria-label="Faint hemp leaf motif"></div>
      <p class="strength">500mg Full Spectrum CBD</p>
    </article>
    <article class="label label--forest label--small" style="left:540px">
      <h2 class="brand-name">LumiVera</h2>
      <p class="tagline">Premium CBD Products</p>
      <p class="flavor">Mint</p>
      <p class="product-name">L Oil</p>
      <div class="leaf-motif" role="img" aria-label="Faint hemp leaf motif"></div>
      <p class="strength">500mg Full Spectrum CBD</p>
    </article>
    <article class="label label--cream label--small" style="left:795px">
      <h2 class="brand-name">LumiVera</h2>
      <p class="tagline">Premium CBD Products</p>
      <p class="flavor">Natural</p>
      <p class="product-name">L Oil</p>
      <div class="leaf-motif" role="img" aria-label="Faint hemp leaf motif"></div>
      <p class="strength">500mg Full Spectrum CBD</p>
    </article>
  </section>

  <section class="row-packs" aria-label="Boxes and labels">
    <article class="box box--cream" style="left:43px">
      <p class="est">Est. 2020</p>
      <div class="mark-dot"></div>
      <h2 class="brand-name">LumiVera</h2>
      <p class="tagline">Premium CBD Products</p>
      <p class="flavor">Natural</p>
      <p class="product-name">L Oil</p>
      <div class="leaf-motif" role="img" aria-label="Large faint hemp leaf motif"></div>
    </article>
    <article class="box box--forest" style="left:294px">
      <p class="est">Est. 2020</p>
      <div class="mark-dot"></div>
      <h2 class="brand-name">LumiVera</h2>
      <p class="tagline">Premium CBD Products</p>
      <p class="flavor">Mint</p>
      <p class="product-name">L Oil</p>
      <div class="leaf-motif" role="img" aria-label="Large faint hemp leaf motif"></div>
    </article>
    <article class="label label--forest label--large" style="left:559px">
      <h2 class="brand-name">LumiVera</h2>
      <p class="tagline">Premium CBD Products</p>
      <p class="flavor">Mint</p>
      <p class="product-name">L Oil</p>
      <div class="leaf-motif" role="img" aria-label="Faint hemp leaf motif"></div>
      <p class="strength">500mg Full Spectrum CBD</p>
    </article>
    <article class="label label--cream label--large" style="left:795px">
      <h2 class="brand-name">LumiVera</h2>
      <p class="tagline">Premium CBD Products</p>
      <p class="flavor">Natural</p>
      <p class="product-name">L Oil</p>
      <div class="leaf-motif" role="img" aria-label="Faint hemp leaf motif"></div>
      <p class="strength">500mg Full Spectrum CBD</p>
    </article>
  </section>
</body>
</html>
```